Flyer for tutoring

The text should be presented in an engaging way to attract potential customers.
Colorfully designed
Around the edge, various objects related to school and the subjects (see text) should be visible.

```html
<!DOCTYPE html>
<html lang="de">
<head>
<meta charset="utf-8">
<title>Nachhilfe Flyer</title>
<link href="https://fonts.googleapis.com/css2?family=Poppins:ital,wght@0,300;0,400;0,500;0,600;0,700;1,400;1,500&display=swap" rel="stylesheet">
<style>
  :root{
    --stage:#616161;
    --green:#9fcd45;
    --green-soft:#e9f3d6;
    --frame-blue:#3a7fd0;
    --navy:#27348b;
    --navy-deep:#15205e;
    --sky:#0b93e6;
    --tab-light:#2aa7e8;
    --red:#e0262b;
    --wine:#a8232a;
    --wine-deep:#5c0b12;
    --leaf:#3d8f2b;
    --yellow:#f7c21b;
    --yellow-light:#fde27a;
    --ink:#222;
    --plum:#2a0f5c;
    --icon-fill:#5b7487;
    --icon-faint:rgba(60,90,60,.22);
  }
  *{margin:0;padding:0;box-sizing:border-box}
  html,body{width:1200px;height:681px;overflow:hidden}
  body{background:var(--stage);font-family:"Poppins",sans-serif;position:relative}

  .flyer{
    position:absolute;left:373px;top:20px;width:453px;height:641px;
    background:linear-gradient(180deg,var(--green) 0%,#b9da74 40%,var(--green-soft) 80%,#fafdf4 100%);
    overflow:hidden;
    box-shadow:0 6px 18px rgba(0,0,0,.35);
  }
  .panel{
    position:absolute;left:31px;top:36px;width:391px;height:567px;
    background:#fff;border:2.5px solid var(--frame-blue);
    border-radius:14px 0 0 0;
  }
  .abs{position:absolute}
  .center{left:0;width:453px;text-align:center;white-space:nowrap}

  .intro{top:58px;color:var(--navy);font-weight:600;font-size:13.8px;line-height:16.5px}

  .tab{
    left:80px;top:97px;width:292px;height:40px;
    background:linear-gradient(180deg,var(--tab-light),#3d7fb0 60%,#4a6f88);
    clip-path:polygon(0 0,100% 0,90% 100%,10% 100%);
    border-radius:4px;
  }
  .banner{
    left:46px;top:109px;width:362px;height:122px;border-radius:13px;
    background:linear-gradient(180deg,var(--navy-deep) 0%,#123f8e 50%,var(--sky) 100%);
  }
  .tab-cover{
    left:80px;top:109px;width:292px;height:28px;
    background:linear-gradient(180deg,#3b8dc6,#4d6f86);
    clip-path:polygon(0 0,100% 0,90% 100%,10% 100%);
  }
  .tab-text{top:104px;color:#fff;font-size:22px;font-weight:400;line-height:26px}
  .title{top:141px;color:#fff;font-weight:700;font-size:28px;line-height:35px;letter-spacing:.2px}
  .title .slash{font-weight:300}

  .brush-yellow{
    background:linear-gradient(90deg,var(--yellow),var(--yellow-light) 45%,var(--yellow));
    clip-path:polygon(2% 18%,8% 0,50% 6%,93% 0,100% 22%,97% 55%,100% 88%,90% 100%,45% 94%,6% 100%,0 80%,3% 50%);
  }
  .slogan-band{left:77px;top:218px;width:299px;height:24px}
  .slogan{top:221px;font-size:12.3px;color:#1d1d3a;line-height:17px}

  .lesson{top:257px;color:var(--navy);font-weight:600;font-size:13.6px;line-height:16px}
  .lesson-time{top:273px;color:var(--red);font-weight:600;font-size:12.8px;line-height:16px}
  .body-copy{left:80px;top:293px;width:293px;font-size:9.3px;line-height:11px;color:var(--ink);text-align:center}

  .rule{height:1px;background:var(--navy);left:89px;width:274px}
  .rule.r1{top:344px}
  .rule.r2{top:504px}

  .eindruck{top:351px;color:var(--leaf);font-weight:600;font-size:13px;line-height:15.5px}

  .brush-red{
    left:68px;top:389px;width:316px;height:45px;
    background:linear-gradient(90deg,var(--wine),#8e1a22 60%,var(--wine-deep));
    clip-path:polygon(1% 14%,6% 0,40% 5%,80% 0,99% 6%,100% 40%,97% 70%,99% 96%,60% 100%,20% 95%,2% 100%,0 60%,2% 35%);
  }
  .motivation{top:395px;color:#fff;font-weight:600;font-size:16px;line-height:17px}

  .person{left:64px;top:449px;width:338px;font-size:9.3px;line-height:11.5px;color:var(--ink)}
  .person-label{position:relative;display:inline-block;font-weight:600;color:var(--navy);font-size:10.5px;line-height:11.5px;padding:0 5px 0 1px;margin-right:6px;z-index:0}
  .person-label::before{content:"";position:absolute;left:-4px;right:-2px;top:1px;bottom:0;z-index:-1;
    background:linear-gradient(90deg,var(--yellow),var(--yellow-light));
    clip-path:polygon(3% 10%,96% 0,100% 70%,94% 100%,5% 92%,0 50%)}
  .subjects{color:var(--red);font-style:italic}
  .math-note{left:64px;top:486px;font-size:9.4px;line-height:12px;color:var(--navy);font-style:italic}

  .contact-band{left:151px;top:510px;width:152px;height:15px}
  .contact-head{top:511px;color:var(--navy);font-weight:600;font-size:10.8px;line-height:14px}

  .pill{left:66px;top:527px;width:320px;height:22px;border-radius:11px;border:1.5px solid var(--wine);background:#fff;overflow:hidden}
  .pill-mail{position:absolute;left:0;top:0;width:208px;height:100%;
    background:linear-gradient(90deg,var(--plum),#4b1760 55%,var(--wine));
    border-radius:11px;display:flex;align-items:center;padding-left:10px;gap:6px;color:#fff;font-size:10.2px;line-height:12px;white-space:nowrap}
  .pill-phone{position:absolute;left:217px;top:0;height:100%;display:flex;align-items:center;gap:6px;color:#1a1a1a;font-weight:600;font-size:10.2px;line-height:12px;white-space:nowrap}

  .reach{top:556px;font-size:10.5px;line-height:14px;color:var(--ink)}
  .thanks{top:572px;font-size:8.8px;line-height:12px;color:var(--wine);font-style:italic}

  .placeholder{position:absolute;border-radius:8px}
  .solid{background:var(--icon-fill)}
  .faint{background:var(--icon-faint);border-radius:5px}
  .round{border-radius:50%}
</style>
</head>
<body>
  <main class="flyer">
    <div class="panel"></div>

    <div class="placeholder faint" style="left:8px;top:7px;width:26px;height:25px" role="img" aria-label="Geodreieck-Zeichnung"></div>
    <div class="placeholder faint" style="left:105px;top:17px;width:37px;height:8px" role="img" aria-label="Bleistift-Zeichnung"></div>
    <div class="placeholder faint round" style="left:195px;top:4px;width:59px;height:31px" role="img" aria-label="Fussball-Umriss"></div>
    <div class="placeholder faint" style="left:308px;top:10px;width:33px;height:17px" role="img" aria-label="Büroklammer-Zeichnung"></div>
    <div class="placeholder faint" style="left:424px;top:119px;width:26px;height:28px" role="img" aria-label="Schachtel-Zeichnung"></div>
    <div class="placeholder faint" style="left:5px;top:207px;width:20px;height:24px" role="img" aria-label="ABC-Würfel-Zeichnung"></div>
    <div class="placeholder faint" style="left:426px;top:241px;width:24px;height:24px" role="img" aria-label="Lineal-Zeichnung"></div>
    <div class="placeholder faint" style="left:9px;top:293px;width:8px;height:38px" role="img" aria-label="Bleistift-Zeichnung"></div>
    <div class="placeholder faint" style="left:426px;top:349px;width:24px;height:26px" role="img" aria-label="Taschenrechner-Zeichnung"></div>
    <div class="placeholder faint" style="left:431px;top:418px;width:12px;height:26px" role="img" aria-label="Büroklammer-Zeichnung"></div>
    <div class="placeholder faint" style="left:5px;top:487px;width:21px;height:26px" role="img" aria-label="Schachtel-Zeichnung"></div>
    <div class="placeholder faint" style="left:426px;top:494px;width:25px;height:26px" role="img" aria-label="Laborkolben-Zeichnung"></div>
    <div class="placeholder faint" style="left:114px;top:609px;width:31px;height:21px" role="img" aria-label="Bleistift-Zeichnung"></div>
    <div class="placeholder faint" style="left:217px;top:605px;width:28px;height:28px" role="img" aria-label="Taschenrechner-Zeichnung"></div>
    <div class="placeholder faint" style="left:313px;top:607px;width:24px;height:26px" role="img" aria-label="ABC-Würfel-Zeichnung"></div>

    <div class="placeholder round" style="left:-14px;top:58px;width:58px;height:58px;background:#e8e8e8;border:2px solid #222" role="img" aria-label="Illustration Fussball"></div>
    <div class="placeholder solid" style="left:369px;top:8px;width:77px;height:57px;background:#7d8790" role="img" aria-label="Illustration Doktorhut"></div>
    <div class="placeholder round" style="left:384px;top:279px;width:60px;height:58px;background:linear-gradient(135deg,#eee,#c9c9c9)" role="img" aria-label="Illustration Farbpalette mit Pinsel"></div>
    <div class="placeholder" style="left:6px;top:373px;width:46px;height:48px;background:linear-gradient(180deg,#e6eef4,#3a8fd6)" role="img" aria-label="Illustration Laborkolben"></div>
    <div class="placeholder solid" style="left:12px;top:583px;width:40px;height:47px" role="img" aria-label="Illustration Buch"></div>
    <div class="placeholder solid" style="left:385px;top:568px;width:56px;height:69px;border-radius:16px 16px 8px 8px" role="img" aria-label="Illustration Schulrucksack"></div>

    <p class="abs center intro">Möchtest du dich gerne in der Schule<br>verbessern und suchst eine</p>
    <div class="abs tab"></div>
    <div class="abs banner"></div>
    <div class="abs tab-cover"></div>
    <p class="abs center tab-text">Professionelle</p>
    <h1 class="abs center title">NACHHILFELEHRERIN <span class="slash">/</span><br>LERNCOACH ?</h1>
    <div class="abs brush-yellow slogan-band"></div>
    <p class="abs center slogan">Dann lass es uns doch mal versuchen!</p>

    <h2 class="abs center lesson">Die erste Lektion – die Kennenlernlektion</h2>
    <p class="abs center lesson-time">– dauert ca. 30 Minuten.</p>
    <p class="abs body-copy">Sie ist kostenlos. Denn wir müssen ja sicher gehen, dass wir uns verstehen und leiden können. Bei unserem ersten Treffen legen wir auch fest, woran wir arbeiten werden und wann die Nachhilfe in deine Agenda passt.</p>
    <div class="abs rule r1"></div>

    <p class="abs center eindruck">Wenn der erste Eindruck stimmt, dann legen wir los,<br>und bald schon werden</p>
    <div class="abs brush-red"></div>
    <p class="abs center motivation">deine Motivation und deine<br>Noten besser und besser!</p>

    <p class="abs person"><span class="person-label">Zu meiner Person:</span> Ich wohne hier in der Siedlung Lindenweg und bin ausgebildete und sehr erfahrene Sekundar- und Primarlehrerin in den Fächern Deutsch, <span class="subjects">Französisch, Englisch und Geschichte.</span></p>
    <p class="abs math-note">(Auf Wunsch auch Mathe-Nachhilfe möglich.)</p>
    <div class="abs rule r2"></div>

    <div class="abs brush-yellow contact-band"></div>
    <p class="abs center contact-head">Meine Kontaktdaten:</p>
    <div class="abs pill">
      <div class="pill-mail">
        <svg width="15" height="11" viewBox="0 0 15 11" aria-hidden="true"><rect x=".5" y=".5" width="14" height="10" rx="1" fill="#f7c21b"/><path d="M1 1l6.5 5L14 1" fill="none" stroke="#2a0f5c" stroke-width="1.2"/></svg>
        <span>mara.lindauer@beispielmail.ch</span>
      </div>
      <div class="pill-phone">
        <svg width="11" height="11" viewBox="0 0 24 24" aria-hidden="true"><path fill="#a8232a" d="M6.6 10.8a15.1 15.1 0 0 0 6.6 6.6l2.2-2.2c.3-.3.7-.4 1-.2 1.1.4 2.3.6 3.6.6.6 0 1 .4 1 1V20c0 .6-.4 1-1 1A17 17 0 0 1 3 4c0-.6.4-1 1-1h3.5c.6 0 1 .4 1 1 0 1.3.2 2.5.6 3.6.1.3 0 .7-.2 1z"/></svg>
        <span>079 555 18 42</span>
      </div>
    </div>
    <p class="abs center reach">(nachmittags fast immer erreichbar)</p>
    <p class="abs center thanks">Ich freue mich auf deine Kontaktaufnahme! Bis bald!</p>
  </main>
</body>
</html>
```